Beekeeper needs box/label design for honey/CBD and other honey-related products

We need a box (or label) design for a beekeeping company in Virginia called Larkmoor Hollow Farm. Our products will include honey mixed with CBD oil and other essential oils (vanilla, lavender, etc).The box design should be scalable to include several different honey/oil products. We would like to incorporate our current farm logo into the design. Here is a link to a honey producing company with a series of products using their honey mixed with certain oils. It's a good reference of what type box/label design we would like (https://pipandwrenly.co/pages/honey).

Target Market(s)

Retail stores and consumers

Requirements
Must have
• Larkmoor Hollow Farm name and logo

```html
<!DOCTYPE html>
<html lang="en">
<head>
<meta charset="utf-8">
<title>Larkmoor Hollow Farm – CBD Honey Label</title>
<link rel="stylesheet" href="https://fonts.googleapis.com/css2?family=Cinzel:wght@500&family=Barlow:wght@500&family=Barlow+Semi+Condensed:wght@500;600&display=swap">
<style>
  :root {
    --page-bg: #f6f6f6;
    --label-top: #e9e9e9;
    --label-bottom: #dadada;
    --olive: #6a6d2a;
    --olive-light: #8c9a3a;
    --cbd-tint: #c4c8a6;
    --ink: #262626;
  }
  html, body {
    margin: 0;
    padding: 0;
    width: 1200px;
    height: 1200px;
    overflow: hidden;
    background: var(--page-bg);
  }
  .label {
    position: absolute;
    left: 280px;
    top: 148px;
    width: 640px;
    height: 904px;
    overflow: hidden;
    background: linear-gradient(180deg, var(--label-top) 0%, var(--label-bottom) 100%);
  }
  .brand-mark {
    position: absolute;
    left: 190px;
    top: 34px;
    width: 260px;
    height: 258px;
    box-sizing: border-box;
    border: 9px solid var(--olive);
  }
  .brand-name {
    position: absolute;
    left: 0;
    width: 100%;
    text-align: center;
    font-family: "Cinzel", serif;
    font-weight: 500;
    color: var(--olive);
    line-height: 1;
    margin: 0;
  }
  .brand-name__main {
    top: 330px;
    font-size: 78px;
    letter-spacing: 1px;
  }
  .brand-name__sub {
    top: 437px;
    font-size: 32px;
    letter-spacing: 6px;
  }
  .product-cbd {
    position: absolute;
    left: 0;
    top: 448px;
    width: 100%;
    text-align: center;
    font-family: "Barlow", sans-serif;
    font-weight: 500;
    font-size: 260px;
    line-height: 1;
    letter-spacing: 4px;
    color: var(--cbd-tint);
    margin: 0;
  }
  .product-name {
    position: absolute;
    left: 0;
    top: 696px;
    width: 100%;
    text-align: center;
    font-family: "Barlow Semi Condensed", sans-serif;
    font-weight: 500;
    font-size: 82px;
    line-height: 1;
    color: var(--ink);
    margin: 0;
  }
  .product-variant {
    position: absolute;
    left: 213px;
    top: 784px;
    font-family: "Barlow Semi Condensed", sans-serif;
    font-weight: 500;
    font-size: 32px;
    line-height: 1;
    color: var(--ink);
    margin: 0;
  }
  .net-weight {
    position: absolute;
    left: 588px;
    top: 734px;
    writing-mode: vertical-rl;
    transform: rotate(180deg);
    font-family: "Barlow Semi Condensed", sans-serif;
    font-weight: 600;
    font-size: 24px;
    line-height: 1;
    color: var(--olive-light);
    white-space: nowrap;
    margin: 0;
  }
</style>
</head>
<body>
  <main class="label">
    <div class="brand-mark" aria-hidden="true"></div>
    <p class="brand-name brand-name__main">LARKMOOR</p>
    <p class="brand-name brand-name__sub">HOLLOW FARM</p>
    <p class="product-cbd">CBD</p>
    <h1 class="product-name">Honey Mixed</h1>
    <p class="product-variant">Essential Oil</p>
    <p class="net-weight">Net Wt: 200g</p>
  </main>
</body>
</html>
```